co working space / serviced office/ business centre

Brivlo - brivlo.in, is a very young brand bieng run by 3 young entrepreneurs. We want to be become out of the league company delivering fabulous and beautiful serviced offices in India and abroad. We hire designers who have made spaces across the world. We want to get visiting card design which gives complete fresh look to the people who carries that card, has to be very impactful and should symbolise happy young and energetic brand. should be completely out of the box thinking of international level, should portray global brand image.

Target Market(s)

Startups, (Small, medium and large corporates)

Industry/Entity Type

Business

Contact Information for Business Card

Name, Email, Address, Mobile number, Landline number, website

Colors

Designer to choose colors to be used in the design.

Requirements
Must have
• Nice new shape
Nice to have
• We want creative cuts, different size and impactful brand clarity
Should not have
• Boring and regular design and shape

```html
<!DOCTYPE html>
<html lang="en">
<head>
<meta charset="utf-8">
<title>Brivlo – Business Cards</title>
<link rel="stylesheet" href="https://fonts.googleapis.com/css2?family=Lato:wght@400;700&family=Michroma&display=swap">
<style>
  :root {
    --backdrop: #5f5f5f;
    --brand-red: #ec1c24;
    --paper: #ffffff;
    --ink: #1a1a1a;
    --rule: #d6d6d6;
  }
  html, body {
    margin: 0;
    width: 1200px;
    height: 1200px;
    overflow: hidden;
    background: var(--backdrop);
  }
  .sheet { position: relative; width: 1200px; height: 1200px; }
  .card { position: absolute; width: 554px; height: 352px; }
  .card--front { left: 38px; }
  .card--back { left: 608px; }
  .row-1 { top: 44px; }
  .row-2 { top: 414px; }
  .row-3 { top: 784px; }
  .shape-paper { fill: var(--paper); }
  .shape-red { fill: var(--brand-red); }
  .mini-brand { font-family: "Michroma", sans-serif; font-size: 20px; fill: var(--brand-red); }
  .person-name { font-family: "Michroma", sans-serif; font-size: 21px; fill: var(--ink); stroke: var(--ink); stroke-width: 0.5; }
  .person-role { font-family: "Michroma", sans-serif; font-size: 11px; fill: var(--brand-red); }
  .contact { font-family: "Lato", sans-serif; font-size: 19px; fill: var(--ink); }
  .address { font-family: "Lato", sans-serif; font-size: 19px; fill: var(--paper); }
  .icon { fill: none; stroke: var(--ink); stroke-width: 1.4; }
  .icon-fill { fill: var(--ink); }
  .big-brand { font-family: "Michroma", sans-serif; font-size: 70px; fill: var(--paper); stroke: var(--paper); stroke-width: 3; }
  .tagline { font-family: "Michroma", sans-serif; font-size: 23px; fill: var(--paper); stroke: var(--paper); stroke-width: 0.8; }
</style>
</head>
<body>
<svg width="0" height="0" style="position:absolute" aria-hidden="true">
  <defs>
    <path id="card-outline" d="M0,120 C0,98 20,88 50,82 L198,60 A82,82 0 0 1 356,60 L504,82 C534,88 554,98 554,120 L554,330 Q554,352 532,352 L22,352 Q0,352 0,330 Z"/>
    <clipPath id="card-clip"><use href="#card-outline"/></clipPath>
    <g id="contact-block">
      <circle class="icon" cx="94" cy="249" r="8"/>
      <rect class="icon" x="91" y="244" width="6" height="10" rx="1"/>
      <text class="contact" x="110" y="256">+91 000 000 0000</text>
      <circle class="icon" cx="94" cy="273" r="8"/>
      <path class="icon" d="M90,269 q0,8 8,8 l1,-2 l-2,-2 l-2,1 q-2,-1 -3,-3 l1,-2 l-2,-2 z"/>
      <text class="contact" x="110" y="280">+91 900 123 4567</text>
      <circle class="icon" cx="312" cy="249" r="8"/>
      <rect class="icon-fill" x="308" y="246" width="8" height="6" rx="1"/>
      <text class="contact" x="329" y="256">name@brivlo.in</text>
      <circle class="icon" cx="312" cy="273" r="8"/>
      <ellipse class="icon" cx="312" cy="273" rx="3.5" ry="8"/>
      <line class="icon" x1="304" y1="273" x2="320" y2="273"/>
      <text class="contact" x="329" y="280">www.brivlo.in</text>
    </g>
    <g id="front-frame">
      <use href="#card-outline" class="shape-paper"/>
      <path class="shape-red" clip-path="url(#card-clip)" d="M0,286 Q277,316 554,286 L554,352 L0,352 Z"/>
      <text class="mini-brand" x="277" y="70" text-anchor="middle">BRIVLO</text>
      <line x1="136" y1="206" x2="416" y2="206" stroke="var(--rule)" stroke-width="1.5"/>
      <use href="#contact-block"/>
      <text class="address" x="277" y="327" text-anchor="middle">Building 7C, Lotus Park, Gurugram, India</text>
    </g>
    <g id="back-face">
      <use href="#card-outline" class="shape-red"/>
      <text class="big-brand" x="277" y="232" text-anchor="middle" textLength="476" lengthAdjust="spacingAndGlyphs">BRIVLO</text>
      <rect x="37" y="262" width="480" height="4" fill="var(--paper)"/>
      <text class="tagline" x="277" y="311" text-anchor="middle" textLength="342" lengthAdjust="spacingAndGlyphs">MEET. PLAN. GROW</text>
    </g>
  </defs>
</svg>

<main class="sheet">
  <svg class="card card--front row-1" viewBox="0 0 554 352" aria-label="Business card front, Rohan Mehra">
    <use href="#front-frame"/>
    <text class="person-name" x="277" y="154" text-anchor="middle" textLength="312" lengthAdjust="spacingAndGlyphs">ROHAN MEHRA</text>
    <text class="person-role" x="277" y="173" text-anchor="middle" textLength="154" lengthAdjust="spacingAndGlyphs">FOUNDER &amp; CEO</text>
  </svg>
  <svg class="card card--back row-1" viewBox="0 0 554 352" aria-label="Business card back"><use href="#back-face"/></svg>

  <svg class="card card--front row-2" viewBox="0 0 554 352" aria-label="Business card front, Vikram Desai">
    <use href="#front-frame"/>
    <text class="person-name" x="277" y="154" text-anchor="middle" textLength="240" lengthAdjust="spacingAndGlyphs">VIKRAM DESAI</text>
    <text class="person-role" x="277" y="173" text-anchor="middle" textLength="154" lengthAdjust="spacingAndGlyphs">FOUNDER &amp; CAO</text>
  </svg>
  <svg class="card card--back row-2" viewBox="0 0 554 352" aria-label="Business card back"><use href="#back-face"/></svg>

  <svg class="card card--front row-3" viewBox="0 0 554 352" aria-label="Business card front, Karan Bhatia">
    <use href="#front-frame"/>
    <text class="person-name" x="277" y="154" text-anchor="middle" textLength="244" lengthAdjust="spacingAndGlyphs">KARAN BHATIA</text>
    <text class="person-role" x="277" y="173" text-anchor="middle" textLength="154" lengthAdjust="spacingAndGlyphs">FOUNDER &amp; COO</text>
  </svg>
  <svg class="card card--back row-3" viewBox="0 0 554 352" aria-label="Business card back"><use href="#back-face"/></svg>
</main>
</body>
</html>
```